Label Design for honey from a small farm in Italy

We need a label for our Acacia's honey .
We are a little farm in Italy and we would like something like organic, raw and simple.
Maybe with botanical drawing with different color like watercolor o something like that (very important natural and easy)
the jar for 1kg of honey: Capacity: 780 ml - Height: 137 mm - Diameter: ∅ 94 mm
- size approx h 5,5 x 10/14cm ( we use the same label for kg and 500 gr jar)

Industry/Entity Type

Farm

Requirements
Must have
• the writings:
- Acacia
- Miele italiano di Acacia
- Da consumarsi preferibilmente entro: ( and below the space to put the date by the hands)
- some space to put some presentation of the farm or some phrases
- our logo
- the space to put the weight by the hands
- Prodotto da Azienda Agricola ...(produced by Farm Name and address....)
- Confezionato presso Apicoltura... (packaged at apiculture Name and address..)
- graphic of Acacia’s flowers ( like drawing)
Should not have
• Barcode
nutritional table

```html
<!DOCTYPE html>
<html lang="it">
<head>
<meta charset="utf-8">
<title>Etichetta Miele di Acacia</title>
<link href="https://fonts.googleapis.com/css2?family=Yellowtail&family=Oswald:wght@300&family=Manrope:wght@500&display=swap" rel="stylesheet">
<style>
  :root {
    --ink: #546b64;
    --mint: #c7e6db;
    --mint-soft: #d6eee5;
    --frame: #555555;
    --paper: #ffffff;
  }
  html, body {
    margin: 0;
    padding: 0;
    width: 1200px;
    height: 1147px;
    overflow: hidden;
    background: var(--paper);
  }
  .canvas {
    position: relative;
    width: 1200px;
    height: 1147px;
  }
  .label {
    position: absolute;
    width: 1067px;
    height: 614px;
    box-sizing: border-box;
    border: 1px solid var(--frame);
    background: var(--paper);
    overflow: hidden;
    transform-origin: 0 0;
    color: var(--ink);
  }
  .label--large { left: 132px; top: 80px; }
  .label--small { left: 441px; top: 887px; transform: scale(0.4207); }

  .botanical {
    position: absolute;
    left: 0;
    top: 0;
    width: 520px;
    height: 600px;
  }
  .centre-block {
    position: absolute;
    left: 266px;
    width: 534px;
    margin: 0;
    text-align: center;
  }
  .title {
    top: 128px;
    font-family: "Yellowtail", cursive;
    font-weight: 400;
    font-size: 134px;
    line-height: 1;
    color: var(--ink);
    text-shadow: 4px 5px 0 var(--paper), 7px 9px 0 var(--ink);
  }
  .subtitle {
    top: 302px;
    font-family: "Oswald", sans-serif;
    font-weight: 300;
    font-size: 47px;
    line-height: 1.1;
  }
  .producer {
    top: 388px;
    font-family: "Manrope", sans-serif;
    font-weight: 500;
    font-size: 26px;
    line-height: 23px;
  }
  .note {
    position: absolute;
    top: 479px;
    margin: 0;
    font-family: "Manrope", sans-serif;
    font-weight: 500;
    font-size: 17px;
    line-height: 24px;
  }
  .note--expiry { left: 72px; }
  .note--packer { left: 741px; }
  .farm-mark {
    position: absolute;
    left: 452px;
    top: 502px;
    width: 180px;
    display: flex;
    align-items: center;
    gap: 8px;
    font-family: "Manrope", sans-serif;
    font-weight: 500;
    font-size: 19px;
    color: var(--mint);
    white-space: nowrap;
  }
  .farm-mark__dot {
    width: 14px;
    height: 14px;
    border-radius: 50%;
    background: var(--mint);
    flex: none;
  }
</style>
</head>
<body>
<div class="canvas">

  <section class="label label--large">
    <svg class="botanical" viewBox="0 0 520 600" role="img" aria-label="Illustrazione botanica: ramo di fiori e foglie di acacia su pennellata ad acquerello verde acqua">
      <defs>
        <linearGradient id="wash-large" x1="0" y1="0" x2="1" y2="1">
          <stop offset="0" stop-color="#c7e6db"/>
          <stop offset="1" stop-color="#d6eee5"/>
        </linearGradient>
      </defs>
      <path fill="url(#wash-large)" d="M0 0 L290 0 C330 40 380 80 400 105 C440 150 470 200 490 260 C505 310 508 360 498 410 L470 440 L452 470 L440 430 L420 470 L395 452 L380 500 L355 470 L335 535 L305 520 L280 570 L250 585 L235 540 L215 565 L195 520 L178 560 L165 470 C140 410 110 360 80 300 C55 250 30 200 0 140 Z"/>
    </svg>
    <h1 class="centre-block title">Acacia</h1>
    <p class="centre-block subtitle">Miele italiano di Acacia</p>
    <p class="centre-block producer">Prodotto da Azienda<br>Agricola</p>
    <p class="note note--expiry">Da consumarsi&nbsp; preferibilmente entro:</p>
    <p class="note note--packer">Confezionato presso Apicoltura</p>
    <div class="farm-mark"><span class="farm-mark__dot"></span>Podere Vallefiorita</div>
  </section>

  <section class="label label--small">
    <svg class="botanical" viewBox="0 0 520 600" role="img" aria-label="Illustrazione botanica: ramo di fiori e foglie di acacia su pennellata ad acquerello verde acqua">
      <defs>
        <linearGradient id="wash-small" x1="0" y1="0" x2="1" y2="1">
          <stop offset="0" stop-color="#c7e6db"/>
          <stop offset="1" stop-color="#d6eee5"/>
        </linearGradient>
      </defs>
      <path fill="url(#wash-small)" d="M0 0 L290 0 C330 40 380 80 400 105 C440 150 470 200 490 260 C505 310 508 360 498 410 L470 440 L452 470 L440 430 L420 470 L395 452 L380 500 L355 470 L335 535 L305 520 L280 570 L250 585 L235 540 L215 565 L195 520 L178 560 L165 470 C140 410 110 360 80 300 C55 250 30 200 0 140 Z"/>
    </svg>
    <h2 class="centre-block title">Acacia</h2>
    <p class="centre-block subtitle">Miele italiano di Acacia</p>
    <p class="centre-block producer">Prodotto da Azienda<br>Agricola</p>
    <p class="note note--expiry">Da consumarsi&nbsp; preferibilmente entro:</p>
    <p class="note note--packer">Confezionato presso Apicoltura</p>
    <div class="farm-mark"><span class="farm-mark__dot"></span>Podere Vallefiorita</div>
  </section>

</div>
</body>
</html>
```